Lumo Pharma Chinese Traditional Medicine Web Design

We need a web design for a new company based in Shanghai China called 'Lumo Pharma'. We develop Chinese traditional herbal medicine, including research and development, technical support service, manufacturing, . Also, there’s a small ratio of western medicine. Our goal is to contributing to a healthier future.

Target Market(s)

global,but mainly China

Industry/Entity Type

Pharmaceutical

Number of Pages Required

1 page

Font styles to use
Serif

Colors
e4daeb
cedeed
cadf82
eaf2ce
fbd4d5
fee3d4
fabb94
fee18a
b8a6cd

Requirements
Must have
• triditional Chinese elements, concept of herbal, health, value, better life for people..could be colourful but not more than 3 different colour..
Nice to have
• Style: simple, communicate traditional Chinese herbal medicine element, as well as modern technique..same as LOGO style..
Should not have
• please dont show more IT elements...

```html
<!DOCTYPE html>
<html lang="en">
<head>
<meta charset="utf-8">
<title>Lumo Pharma — Products</title>
<link href="https://fonts.googleapis.com/css2?family=Gelasio:wght@400;500&family=Open+Sans:wght@400&display=swap" rel="stylesheet">
<style>
:root{
  --green:#3d4740;
  --green-ring:#9aa19b;
  --brown:#5e3425;
  --ink:#4a4a4a;
  --nav:#6b6b6b;
  --paper:#f0eeec;
  --footer:#f3f2f0;
  --white:#ffffff;
  --rule:#c9b8b0;
}
*{margin:0;padding:0;box-sizing:border-box}
html,body{width:782px;height:1200px;overflow:hidden;background:var(--white)}
body{position:relative;font-family:"Open Sans",Arial,sans-serif;color:var(--ink)}
.abs{position:absolute}
.serif{font-family:"Gelasio",Georgia,serif}

.site-header{left:0;top:0;width:782px;height:62px;background:var(--white)}
.brand{display:flex;align-items:center;gap:6px;color:var(--brown);font-family:"Gelasio",Georgia,serif}
.brand-dot{border-radius:50%;background:var(--green)}
.header-brand{left:80px;top:21px;font-size:11px}
.header-brand .brand-dot{width:16px;height:16px}
.main-nav{top:24px;left:242px;display:flex;gap:0;font-family:"Gelasio",Georgia,serif;font-size:11px;color:var(--nav);letter-spacing:.2px}
.main-nav span{position:absolute;white-space:nowrap}
.main-nav .active{color:#444}

.hero{left:0;top:62px;width:782px;height:275px;background:linear-gradient(100deg,#3a3d46 0%,#6e5a48 35%,#a4714e 55%,#5a3a36 75%,#8f2e2e 100%)}
.hero-badge{left:81px;top:117px;width:181px;height:181px;border-radius:50%;background:var(--green);opacity:.96}
.hero-ring{left:86px;top:122px;width:171px;height:171px;border-radius:50%;border:4px solid var(--green-ring)}
.hero-title{left:81px;top:193px;width:181px;text-align:center;color:var(--white);font-size:21px}

.research{left:0;top:337px;width:782px;height:342px;background:var(--paper)}
.research-photo{left:68px;top:366px;width:274px;height:274px;border-radius:50%;background:radial-gradient(circle,#f2ede6 0%,#e6d5c0 45%,#c79a6a 100%)}
.research-title{left:368px;top:432px;font-size:20.5px;color:var(--brown);white-space:nowrap}
.research-copy{left:372px;top:470px;width:324px;font-size:9.4px;line-height:15.3px}
.research-copy p+p{margin-top:15.3px}

.support{left:0;top:679px;width:782px;height:275px;background:var(--green)}
.support-title{left:0;top:733px;width:782px;text-align:center;color:var(--white);font-size:23px}
.support-copy{left:131px;top:779px;width:520px;text-align:center;color:#e8ebe8;font-size:10px;line-height:15.2px}
.support-copy p+p{margin-top:15.2px}

.site-footer{left:0;top:954px;width:782px;height:246px;background:var(--footer)}
.footer-brand{left:78px;top:1020px;font-size:12px}
.footer-brand .brand-dot{width:22px;height:22px}
.registration{left:81px;top:1056px;font-size:11px;line-height:19.5px;color:#333}
.col-title{top:989px;font-family:"Gelasio",Georgia,serif;font-size:12px;color:var(--brown);white-space:nowrap}
.col-links{font-size:10.5px;line-height:20.2px;color:#333}
.address{left:543px;top:1013px;font-size:10.5px;line-height:15px;color:#333}
.social{left:521px;top:1059px;display:flex;gap:3px}
.social span{width:25px;height:25px;border-radius:50%;border:1.5px solid var(--brown)}
.footer-rule{left:70px;top:1145px;width:628px;height:1px;background:var(--rule)}
.copyright{left:0;top:1158px;width:760px;text-align:center;font-size:9px;color:#333}
</style>
</head>
<body>

<header class="abs site-header">
  <div class="abs brand header-brand"><span class="brand-dot"></span>LUMO PHARMA</div>
  <nav class="abs main-nav">
    <span class="active" style="left:0">HOME</span>
    <span style="left:53px">COMPANY OVERALL</span>
    <span style="left:181px">NEWS</span>
    <span style="left:232px">PRODUCTS</span>
    <span style="left:313px">SERVICES</span>
    <span style="left:385px">CAREER</span>
    <span style="left:448px">CONTACT</span>
  </nav>
</header>

<section class="abs hero" role="img" aria-label="Dried Chinese herbs on a dark wooden table: roots, rosebuds, goji berries and ginger slices"></section>
<div class="abs hero-badge"></div>
<div class="abs hero-ring"></div>
<h1 class="abs hero-title serif" style="font-weight:400">PRODUCTS</h1>

<section class="abs research"></section>
<div class="abs research-photo" role="img" aria-label="Herbal ingredients arranged in white spoons on a round bamboo mat"></div>
<h2 class="abs research-title serif" style="font-weight:400">RESEARCH AND DEVELOPMENT</h2>
<div class="abs research-copy">
  <p>hendrerit quis leo Pellentesque rutrum malesuada neque Nunc tempus felis vitae urna Vivamus porttitor neque at volutpat rutrum purus nisi eleifend libero a tempus libero lectus feugiat felis Morbi diam mauris viverra in gravida eu mattis in ante Morbi eget arcu</p>
  <p>Morbi porta libero id ullamcorper nonummy nibh ligula pulvinar metus eget consectetuer augue nisi quis lacus Ut ac mi quis lacus mollis aliquam Curabitur iaculis tempus eros Curabitur vel mi sit amet magna malesuada ultrices Ut nisi erat fermentum vel congue id euismod in elit</p>
</div>

<section class="abs support"></section>
<h2 class="abs support-title serif" style="font-weight:400">TECHNICAL SUPPORT</h2>
<div class="abs support-copy">
  <p>hendrerit quis leo Pellentesque rutrum malesuada neque Nunc tempus felis vitae urna Vivamus porttitor neque at volutpat rutrum purus nisi eleifend libero a tempus libero lectus feugiat felis Morbi diam mauris viverra in gravida eu mattis in ante Morbi eget arcu</p>
  <p>Morbi porta libero id ullamcorper nonummy nibh ligula pulvinar metus eget consectetuer augue nisi quis lacus Ut ac mi quis lacus mollis aliquam Curabitur iaculis tempus eros Curabitur vel mi sit amet magna malesuada ultrices Ut nisi erat fermentum vel congue id euismod in elit</p>
</div>

<footer class="abs site-footer"></footer>
<div class="abs brand footer-brand"><span class="brand-dot"></span>LUMO PHARMA</div>
<div class="abs registration">Registration no.<br>12010000000000</div>

<div class="abs col-title" style="left:275px">QUICK LINKS</div>
<div class="abs col-links" style="left:278px;top:1011px">Home<br>Company overall<br>News<br>Products</div>

<div class="abs col-title" style="left:411px">RESOURCES</div>
<div class="abs col-links" style="left:416px;top:1012px">Services<br>Career<br>Contact</div>

<div class="abs col-title" style="left:525px">OUR ADDRESS</div>
<svg class="abs" style="left:523px;top:1013px" width="16" height="22" viewBox="0 0 16 22" aria-hidden="true">
  <path d="M8 0C3.6 0 0 3.5 0 7.9 0 13.5 8 22 8 22s8-8.5 8-14.1C16 3.5 12.4 0 8 0z" fill="#6b2c22"/>
  <circle cx="8" cy="8" r="3" fill="#f3f2f0"/>
</svg>
<div class="abs address">128 Lanting Road, China<br>(Shanghai) Harbor Trade Zone)</div>
<div class="abs social"><span></span><span></span><span></span><span></span></div>

<div class="abs footer-rule"></div>
<div class="abs copyright">© 2020 Company Name &nbsp;| All Rights Reserved</div>

</body>
</html>
```